Pruett Family Motto/Mission Statement

We are creating a poster to be hung in our home with several purpose statements for our family (last name Pruett, and "The Pruett Family" should be included in the poster prominently). The text that we want included is in the attached file.

Our kids range in age from 8 to 17, so we are looking for something that is homey and cheerful, but fairly bold and oriented to older kids (and not so much younger kids).

I've attached a couple of example poster/statements that we generally like. Overall color scheme could include blues and greens and possibly some brown.

Anticipated size of this poster would be 18"x24" with a portrait orientation.

```html
<!DOCTYPE html>
<html lang="en">
<head>
<meta charset="utf-8">
<title>The Pruett Family</title>
<link rel="stylesheet" href="https://fonts.googleapis.com/css2?family=Fira+Sans:wght@700&family=Nunito+Sans:wght@400;800&display=swap">
<style>
  :root {
    --kraft: #c8a579;
    --kraft-light: #d2b188;
    --kraft-dark: #bb9668;
    --navy: #1c1a86;
    --frame: #1f1fa0;
  }
  html, body {
    margin: 0;
    padding: 0;
    width: 848px;
    height: 1200px;
    overflow: hidden;
    background: var(--kraft);
  }
  .poster {
    position: relative;
    width: 848px;
    height: 1200px;
    box-sizing: border-box;
    border: 10px solid var(--frame);
    background: radial-gradient(ellipse at 50% 40%, var(--kraft-light), var(--kraft) 60%, var(--kraft-dark));
    color: var(--navy);
    font-family: "Nunito Sans", "Helvetica Neue", Arial, sans-serif;
    font-size: 34px;
    line-height: 43px;
    letter-spacing: 0.3px;
  }
  .title {
    position: absolute;
    left: 98px;
    top: 80px;
    width: 640px;
    margin: 0;
    text-align: center;
    font-family: "Fira Sans", "Helvetica Neue", Arial, sans-serif;
    font-weight: 700;
    font-size: 70px;
    line-height: 70px;
    letter-spacing: 3px;
    padding-bottom: 6px;
    border-bottom: 4px solid var(--navy);
  }
  .value {
    position: absolute;
    margin: 0;
    font-weight: 400;
  }
  .value strong { font-weight: 800; }
  .icon {
    position: absolute;
    fill: none;
    stroke: var(--navy);
    stroke-width: 3;
    stroke-linecap: round;
    stroke-linejoin: round;
  }
  .value--learn { left: 124px; top: 246px; display: flex; align-items: center; }
  .learn-book {
    position: relative;
    width: 132px;
    height: 94px;
    margin: 0 6px;
    display: flex;
    align-items: center;
    justify-content: center;
  }
  .learn-book svg { position: absolute; inset: 0; }
  .learn-book strong { position: relative; }
  .value--positive { left: 75px; top: 338px; width: 700px; }
  .value--kindness { left: 97px; top: 486px; width: 660px; }
  .value--adventure { left: 75px; top: 628px; width: 700px; }
  .value--fit { left: 210px; top: 783px; }
  .value--humor { left: 142px; top: 896px; width: 600px; }
  .value--right { left: 68px; top: 1026px; width: 720px; }
</style>
</head>
<body>
<main class="poster">
  <h1 class="title">THE PRUETT FAMILY</h1>

  <p class="value value--learn">We love to
    <span class="learn-book">
      <svg width="132" height="94" viewBox="0 0 132 94" aria-hidden="true" class="book-outline">
        <g fill="none" stroke="var(--navy)" stroke-width="2.5" stroke-linejoin="round">
          <path d="M4 6 Q35 -2 66 10 Q97 -2 128 6 V84 Q97 76 66 88 Q35 76 4 84 Z"/>
          <path d="M66 10 V88"/>
          <path d="M2 12 V90 Q35 82 66 92 Q97 82 130 90 V12"/>
        </g>
      </svg>
      <strong>learn</strong>
    </span>
  new things</p>

  <p class="value value--positive">We look at life through a <strong>positive</strong><br>lens</p>
  <svg class="icon" style="left:200px;top:400px" width="95" height="70" viewBox="0 0 95 70" aria-hidden="true">
    <circle cx="62" cy="30" r="22"/>
    <path d="M62 20 V40 M52 30 H72"/>
    <path d="M45 46 L12 62" stroke-width="7"/>
  </svg>

  <p class="value value--kindness"><strong>Kindness</strong> guides our words and<br>deeds</p>
  <svg class="icon" style="left:353px;top:550px" width="60" height="56" viewBox="0 0 60 56" aria-hidden="true">
    <path d="M30 52 C8 36 3 26 3 17 C3 8 10 3 17 3 C24 3 28 8 30 12 C32 8 36 3 43 3 C50 3 57 8 57 17 C57 26 52 36 30 52 Z"/>
  </svg>

  <p class="value value--adventure">We create <strong>adventure</strong> and choose<br>experiences over things</p>
  <svg class="icon" style="left:580px;top:660px" width="170" height="95" viewBox="0 0 170 95" aria-hidden="true">
    <path d="M4 88 C30 70 50 50 70 12 C78 6 84 10 92 22 L104 34 L116 40 L130 56 L150 68 L166 86"/>
    <path d="M96 30 L90 50 M108 40 L104 60 M120 48 L118 66 M134 60 L130 76 M146 68 L144 82"/>
    <path d="M76 70 C82 60 98 60 102 72 C100 80 80 82 76 70 Z" fill="var(--navy)"/>
  </svg>

  <svg class="icon" style="left:80px;top:765px" width="108" height="90" viewBox="0 0 108 90" aria-hidden="true">
    <path d="M3 42 H30 L36 34 L42 50 L52 4 L60 86 L68 34 L76 44 H105"/>
  </svg>
  <p class="value value--fit">We commit to be <strong>fit</strong></p>

  <p class="value value--humor">Our days are brightened by a<br><strong>sense of humor</strong></p>
  <svg class="icon" style="left:540px;top:930px" width="54" height="80" viewBox="0 0 54 80" aria-hidden="true">
    <path d="M20 4 V24 M34 4 V24"/>
    <path d="M6 50 H48 C48 62 38 74 27 74 C16 74 6 62 6 50 Z"/>
  </svg>

  <p class="value value--right">We <strong>do what is right</strong> even when no<br>one is watching</p>
  <svg class="icon" style="left:418px;top:1072px" width="70" height="80" viewBox="0 0 70 80" aria-hidden="true">
    <path d="M4 40 L22 74 L66 4" stroke-width="7"/>
  </svg>
</main>
</body>
</html>
```